Description of Adventure Certificate:
We require a certificate, that will be awarded to winners of competitions and offered to fundraising organisations for a $ value or type of event service we provide.
The certificate will be professionally printed on thick high-quality paper.
Design concept: Adventurous outer border, and exciting theme.
Title: Adventure Certificate (adventurous font)
Content: "Bringing the Thrill of Adventure to you"
Awarded To:..........................................
From:....................................................
Amount / Event: ...................................
Redemption Location:...........................
Expires:.................................................
Events listed near the base of certificate: Community events, Sports celebrations, Team building, School activities, Festivals, Vacation Care, EXPO's, Trade Shows.
Contact: M: 0418 627 349
E: info@tidalkite.com.au
Images: Tidal Kite Logo
Adventure Certificate image
Carabiner

```html
<!DOCTYPE html>
<html lang="en">
<head>
<meta charset="utf-8">
<title>Adventure Certificate – Tidal Kite</title>
<link rel="stylesheet" href="https://fonts.googleapis.com/css2?family=Bangers&family=Cagliostro&display=swap">
<style>
  :root {
    --sky-light: #f7f8fa;
    --sky-mid: #dde1e6;
    --rock-red: #9c3a26;
    --rock-dark: #5e2216;
    --plank-light: #e6c48f;
    --plank-mid: #d3a668;
    --title-tan: #9a6530;
    --title-dark: #3b2716;
    --rule-gold: #b8853c;
    --ink: #2b2620;
    --frame: #8a4a3a;
    --brand-red: #e0301c;
  }
  * { margin: 0; padding: 0; box-sizing: border-box; }
  html, body { width: 1200px; height: 849px; overflow: hidden; background: #ffffff; }
  .certificate {
    position: relative;
    width: 1200px;
    height: 849px;
    overflow: hidden;
    font-family: "Cagliostro", sans-serif;
    color: var(--ink);
    background: radial-gradient(ellipse at 60% 40%, var(--sky-light) 0%, var(--sky-mid) 70%, #c9ced5 100%);
  }
  .sky-backdrop, .climber-photo, .title-plank {
    position: absolute;
  }
  .sky-backdrop { inset: 0; }
  .climber-photo { left: 0; top: 0; width: 330px; height: 849px; }
  .page-frame {
    position: absolute;
    left: 45px; top: 30px;
    width: 1125px; height: 794px;
    border: 1px solid var(--frame);
  }
  .title-plank { left: 392px; top: 48px; width: 696px; height: 192px; }
  .title {
    position: absolute;
    left: 460px; top: 70px;
    font-family: "Bangers", sans-serif;
    line-height: 1;
    letter-spacing: 1px;
  }
  .title-top { display: block; font-size: 64px; color: var(--title-tan); }
  .title-main { display: block; font-size: 92px; color: var(--title-dark); margin-left: 20px; margin-top: -8px; }
  .rule {
    position: absolute;
    left: 342px; width: 798px; height: 2px;
    background: var(--rule-gold);
  }
  .rule-top { top: 261px; }
  .rule-bottom { top: 332px; }
  .tagline {
    position: absolute;
    left: 342px; width: 798px; top: 276px;
    text-align: center;
    font-size: 35px;
    letter-spacing: 1.5px;
  }
  .fields { position: absolute; left: 342px; width: 798px; top: 372px; list-style: none; }
  .field {
    height: 37px;
    text-align: center;
    font-size: 23px;
    letter-spacing: 1.5px;
    white-space: nowrap;
  }
  .services {
    position: absolute;
    left: 330px; width: 820px; top: 566px;
    text-align: center;
    font-size: 24px;
    font-weight: bold;
    letter-spacing: 1.2px;
    line-height: 32px;
  }
  .contact { position: absolute; left: 367px; top: 730px; list-style: none; }
  .contact-item {
    display: flex; align-items: center; gap: 8px;
    height: 34px;
    font-size: 21px; letter-spacing: 1.5px;
  }
  .contact-icon { width: 23px; height: 23px; }
  .brand {
    position: absolute;
    left: 950px; top: 718px;
    display: flex; align-items: center; gap: 10px;
    font-family: "Cagliostro", sans-serif;
    font-size: 38px;
    color: var(--title-dark);
  }
  .brand-dot { width: 40px; height: 40px; border-radius: 50%; background: var(--brand-red); }
</style>
</head>
<body>
<main class="certificate">
  <svg class="sky-backdrop" width="1200" height="849" role="img" aria-label="Soft cloudy sky photograph">
    <defs>
      <radialGradient id="skyGlow" cx="0.45" cy="0.25" r="0.8">
        <stop offset="0" stop-color="#ffffff"/>
        <stop offset="1" stop-color="#d4d8de"/>
      </radialGradient>
    </defs>
    <rect width="1200" height="849" fill="url(#skyGlow)"/>
  </svg>

  <svg class="climber-photo" width="330" height="849" role="img" aria-label="Photo of a child climbing a red rock climbing wall with a safety rope">
    <defs>
      <linearGradient id="rockTone" x1="0" y1="0" x2="1" y2="0">
        <stop offset="0" stop-color="#7a2c1c"/>
        <stop offset="0.6" stop-color="#9c3a26"/>
        <stop offset="1" stop-color="#b5523a"/>
      </linearGradient>
    </defs>
    <path d="M0 0 H110 L170 150 L180 330 L250 560 L300 700 L320 849 H0 Z" fill="url(#rockTone)"/>
  </svg>

  <div class="page-frame"></div>

  <svg class="title-plank" width="696" height="192" role="img" aria-label="Weathered wooden plank sign behind the title">
    <defs>
      <linearGradient id="plankTone" x1="0" y1="0" x2="1" y2="1">
        <stop offset="0" stop-color="#e8c992"/>
        <stop offset="1" stop-color="#cfa062"/>
      </linearGradient>
    </defs>
    <path d="M14 8 L680 4 L668 40 L690 70 L676 110 L694 150 L672 188 L20 184 L6 150 L18 110 L2 70 L16 36 Z" fill="url(#plankTone)"/>
  </svg>

  <h1 class="title">
    <span class="title-top">ADVENTURE</span>
    <span class="title-main">CERTIFICATE</span>
  </h1>

  <div class="rule rule-top"></div>
  <p class="tagline">"Bringing the Thrill of Adventure to you"</p>
  <div class="rule rule-bottom"></div>

  <ul class="fields">
    <li class="field">Awarded To:..................................................................</li>
    <li class="field">From:.............................................................</li>
    <li class="field">Amount / Event: ...........................................</li>
    <li class="field">Redemption Location:................................</li>
    <li class="field">Expires:...........................</li>
  </ul>

  <p class="services">Community events, Sports celebrations, Team building, School<br>activities, Festivals, Vacation Care, EXPO's, Trade Shows.</p>

  <ul class="contact">
    <li class="contact-item">
      <svg class="contact-icon" viewBox="0 0 24 24"><circle cx="12" cy="12" r="12" fill="#c08a4c"/><path d="M8 6 L10 6 L11 9 L9.5 10.5 C10.3 12.3 11.7 13.7 13.5 14.5 L15 13 L18 14 L18 16 C18 17 17 18 16 18 C10.5 17.5 6.5 13.5 6 8 C6 7 7 6 8 6 Z" fill="#ffffff"/></svg>
      <span>: 0418 627 349</span>
    </li>
    <li class="contact-item">
      <svg class="contact-icon" viewBox="0 0 24 24"><circle cx="12" cy="12" r="12" fill="#c08a4c"/><rect x="6" y="8" width="12" height="8" fill="none" stroke="#ffffff" stroke-width="1.4"/><path d="M6 8 L12 13 L18 8" fill="none" stroke="#ffffff" stroke-width="1.4"/></svg>
      <span>: info@tidalkite.com.au</span>
    </li>
  </ul>

  <div class="brand">
    <span>Tidal Kite</span>
    <span class="brand-dot"></span>
  </div>
</main>
</body>
</html>
```